Halverson Earthworks LLC business card design

Excavation company business cards

Contact Information for Business Card

Halverson Earthworks LLC cell phone 208-555-0147 office phone 208-555-0183 halversonearthworksllc@maildrop-example.com Driveways, site prep, retaining walls, septic systems, rock delivery

Colors

Designer to choose colors to be used in the design.

```html
<!DOCTYPE html>
<html lang="en">
<head>
<meta charset="UTF-8">
<title>Halverson Earthworks LLC business card</title>
<link href="https://fonts.googleapis.com/css2?family=Montserrat:wght@400;500;700;800&display=swap" rel="stylesheet">
<style>
  :root {
    --backdrop: #2b2b2d;
    --card-dark: #1b1b1c;
    --card-light: #ffffff;
    --orange: #ef6b1f;
    --ink: #555558;
    --ink-soft: #6a6a6d;
  }
  * { box-sizing: border-box; margin: 0; padding: 0; }
  html, body { width: 1200px; height: 900px; overflow: hidden; }
  body {
    background: var(--backdrop);
    font-family: "Montserrat", sans-serif;
    position: relative;
  }
  .card {
    position: absolute;
    width: 700px;
    height: 400px;
    border-radius: 22px;
    box-shadow: 0 14px 30px rgba(0,0,0,.45);
  }
  .card-front {
    left: 400px; top: 50px;
    background: var(--card-dark);
    display: flex; align-items: center; justify-content: center;
  }
  .brand-mark {
    display: flex; align-items: center; gap: 16px;
    color: var(--orange);
    font-weight: 800;
    text-transform: uppercase;
    letter-spacing: 1px;
  }
  .brand-mark .dot {
    width: 22px; height: 22px; border-radius: 50%;
    background: var(--orange); flex: none;
  }
  .card-front .brand-mark { font-size: 34px; }
  .card-back {
    left: 100px; top: 430px;
    background: var(--card-light);
  }
  .holder { position: absolute; left: 44px; top: 40px; }
  .holder-name {
    color: var(--orange); font-weight: 700; font-size: 28px;
    text-transform: uppercase; letter-spacing: .5px;
  }
  .holder-title { color: var(--ink); font-size: 21px; margin-top: 2px; }
  .card-back .brand-mark {
    position: absolute; right: 40px; top: 140px;
    font-size: 19px; gap: 10px;
  }
  .card-back .brand-mark .dot { width: 14px; height: 14px; }
  .contacts {
    position: absolute; left: 44px; bottom: 44px;
    list-style: none; color: var(--ink); font-size: 20px; line-height: 1.35;
  }
  .contacts li { display: flex; align-items: center; gap: 8px; }
  .contacts svg { width: 14px; height: 14px; flex: none; }
  .contacts .email { font-size: 16px; }
  .services {
    position: absolute; right: 40px; bottom: 36px;
    list-style: none; color: var(--ink-soft); font-size: 20px; line-height: 1.2;
  }
  .services li::before {
    content: ""; display: inline-block; width: 6px; height: 6px;
    border-radius: 50%; background: var(--orange);
    margin-right: 6px; vertical-align: middle; position: relative; top: -6px;
  }
</style>
</head>
<body>
  <section class="card card-front">
    <div class="brand-mark"><span class="dot"></span>Halverson Earthworks LLC</div>
  </section>

  <section class="card card-back">
    <div class="holder">
      <p class="holder-name">Dale Whitford</p>
      <p class="holder-title">Director</p>
    </div>

    <div class="brand-mark"><span class="dot"></span>Halverson Earthworks LLC</div>

    <ul class="contacts">
      <li>
        <svg viewBox="0 0 14 14" aria-hidden="true"><rect x="3.5" y="1" width="7" height="12" rx="1.5" fill="none" stroke="#ef6b1f" stroke-width="1.5"/></svg>
        208-555-0147
      </li>
      <li>
        <svg viewBox="0 0 14 14" aria-hidden="true"><path d="M2 5 Q7 1 12 5 L10.5 6.5 L9 5.2 L5 5.2 L3.5 6.5 Z M3.5 8 H10.5 L11 12.5 H3 Z" fill="#ef6b1f"/></svg>
        208-555-0183
      </li>
      <li class="email">
        <svg viewBox="0 0 14 14" aria-hidden="true"><rect x="1" y="3" width="12" height="8.5" fill="none" stroke="#ef6b1f" stroke-width="1.4"/><path d="M1 3 L7 8 L13 3" fill="none" stroke="#ef6b1f" stroke-width="1.4"/></svg>
        halversonearthworksllc@maildrop-example.com
      </li>
    </ul>

    <ul class="services">
      <li>Driveways,</li>
      <li>site prep,</li>
      <li>retaining walls,</li>
      <li>septic systems,</li>
      <li>rock delivery</li>
    </ul>
  </section>
</body>
</html>
```